Water Tank Decals

We build large water tanks and want to dress them up with decals. The Bellcrest logo on the back of the tank is out logo
It looks like I added the wrong picture.
file:///C:/Users/lemis/Dropbox/My%20PC%20(DESKTOP-3K8RQ2M)/Downloads/IMG_0388-Eraser-Cutter%20(2).jpg
I am sorry this is the picture that should have been sent.

```html
<!DOCTYPE html>
<html lang="en">
<head>
<meta charset="utf-8">
<title>Bellcrest Water Tanker Decal</title>
<link rel="stylesheet" href="https://fonts.googleapis.com/css2?family=Montserrat:wght@800&family=Saira+Condensed:wght@700&display=swap">
<style>
  :root {
    --paper: #ffffff;
    --ink: #141414;
    --stripe-red: #ed1c24;
    --tab-grey: #58595b;
    --cut-line: #29abe2;
  }
  html, body {
    margin: 0;
    padding: 0;
    width: 1200px;
    height: 900px;
    overflow: hidden;
    background: var(--paper);
  }
  .canvas {
    position: relative;
    width: 1200px;
    height: 900px;
    background: var(--paper);
  }
  .decal-sheet {
    position: absolute;
    left: 45px;
    top: 255px;
    width: 1110px;
    height: 389px;
    overflow: visible;
  }
  .cut-line { fill: none; stroke: var(--cut-line); stroke-width: 1.4; }
  .model-tab { fill: var(--tab-grey); }
  .model-number {
    fill: var(--paper);
    font-family: "Saira Condensed", "Arial Narrow", sans-serif;
    font-weight: 700;
    font-size: 36px;
  }
  .red-stripe { fill: var(--stripe-red); }
  .base-band, .hazard-dash { fill: var(--ink); }
  .headline {
    fill: var(--ink);
    font-family: "Montserrat", Arial, sans-serif;
    font-weight: 800;
    font-size: 82px;
  }
  .brand-mark { fill: var(--stripe-red); }
  .brand-name {
    fill: var(--ink);
    font-family: "Montserrat", Arial, sans-serif;
    font-weight: 800;
    font-size: 20px;
  }
</style>
</head>
<body>
<main class="canvas">
  <svg class="decal-sheet" viewBox="0 0 1541 540" xmlns="http://www.w3.org/2000/svg" aria-label="Water tanker side decal layout">
    <polygon class="cut-line" points="0,0 1541,0 1541,540 43,540"/>

    <g class="model-badge">
      <polygon class="model-tab" points="25,317 207,317 229,363 28,363"/>
      <text class="model-number" x="65" y="354" textLength="100" lengthAdjust="spacingAndGlyphs">BC-600</text>
    </g>

    <g class="front-stripes">
      <polygon class="red-stripe" points="34,411 305,411 317,429 36,429"/>
      <polygon class="red-stripe" points="37,444 322,444 335,461 39,461"/>
    </g>

    <text class="headline" x="440" y="466" textLength="694" lengthAdjust="spacingAndGlyphs">WATER TANKER</text>

    <g class="rear-stripes">
      <polygon class="red-stripe" points="1129,388 1213,317 1541,317 1541,334 1213,334 1149,388"/>
      <polygon class="red-stripe" points="1180,388 1226,349 1541,349 1541,367 1225,367 1200,388"/>
    </g>

    <g class="brand">
      <rect class="brand-mark" x="1371" y="400" width="24" height="24"/>
      <text class="brand-name" x="1383" y="455" text-anchor="middle" textLength="116" lengthAdjust="spacingAndGlyphs">BELLCREST</text>
    </g>

    <g class="base-stripe">
      <polygon class="base-band" points="40,506 1276,506 1251,540 43,540"/>
      <polygon class="hazard-dash" points="1296,506 1336,506 1311,540 1271,540"/>
      <polygon class="hazard-dash" points="1356,506 1390,506 1365,540 1331,540"/>
      <polygon class="hazard-dash" points="1408,506 1438,506 1413,540 1383,540"/>
      <polygon class="hazard-dash" points="1454,506 1480,506 1455,540 1429,540"/>
      <polygon class="hazard-dash" points="1497,506 1519,506 1494,540 1472,540"/>
      <polygon class="hazard-dash" points="1541,512 1541,540 1520,540"/>
    </g>
  </svg>
</main>
</body>
</html>
```